DELCOUR ROOFING YARD SIGN

We need a yard sign to put in our customers' yards when we are roofing their home.
Delcour Roofing
438 Fenwick Rd
Lake Charles LA 70615
phone: 337-555-0142

Maybe some verbiage like "Your Hometown Roofing Experts"
or
"Family Owned Since 1956"

```html
<!DOCTYPE html>
<html lang="en">
<head>
<meta charset="utf-8">
<title>Delcour Roofing Yard Sign</title>
<link rel="stylesheet" href="https://fonts.googleapis.com/css2?family=Noto+Serif:ital,wght@0,500;0,800;1,400;1,700&family=Poppins:wght@500;700&display=swap">
<style>
  :root {
    --page-bg: #efefec;
    --sign-white: #ffffff;
    --ink: #0e0e0e;
    --corner-black: #0d0d0d;
    --ridge-light: #e2e2e2;
    --ridge-dark: #a9a9a9;
    --tile-light: #3a3a3a;
    --tile-dark: #111111;
    --band-grey: #e2e2e2;
    --rule-grey: #cfcfcf;
  }
  * { margin: 0; padding: 0; box-sizing: border-box; }
  html, body { width: 1200px; height: 1200px; overflow: hidden; background: var(--page-bg); }
  .sign-frame {
    position: absolute; left: 180px; top: 40px;
    width: 841px; height: 1120px;
    box-shadow: 0 10px 30px rgba(0,0,0,0.15);
  }
  .sign {
    position: absolute; left: 0; top: 0;
    width: 944px; height: 1257px;
    background: var(--sign-white);
    transform: scale(0.891); transform-origin: 0 0;
    overflow: hidden;
  }
  .sign-shapes { position: absolute; left: 0; top: 0; }
  .brand-seal {
    position: absolute; left: 187px; top: 287px;
    width: 316px; height: 316px; border-radius: 50%;
    border: 3px solid var(--ink);
    display: flex; align-items: center; justify-content: center;
    font-family: "Noto Serif", serif; font-weight: 500;
    font-size: 34px; color: var(--ink); text-align: center; line-height: 1.2;
  }
  .company-name {
    position: absolute; left: 0; width: 944px; top: 630px;
    text-align: center;
    font-family: "Noto Serif", serif; font-weight: 800;
    font-size: 148px; line-height: 120px; color: var(--ink);
    letter-spacing: -2px;
  }
  .company-name span { display: block; }
  .tagline {
    position: absolute; left: 0; width: 944px; top: 905px;
    text-align: center;
    font-family: "Noto Serif", serif; font-style: italic; font-weight: 400;
    font-size: 40px; color: var(--ink);
  }
  .tagline-rule {
    position: absolute; left: 177px; width: 590px; top: 970px;
    height: 2px; background: var(--rule-grey);
  }
  .phone {
    position: absolute; left: 0; width: 944px; top: 980px;
    display: flex; align-items: center; justify-content: center; gap: 14px;
    font-family: "Poppins", sans-serif; font-weight: 700;
    font-size: 78px; color: var(--ink); line-height: 1.1;
  }
  .phone svg { width: 60px; height: 60px; }
  .since {
    position: absolute; left: 0; width: 944px; top: 1065px;
    text-align: center;
    font-family: "Noto Serif", serif; font-style: italic; font-weight: 700;
    font-size: 36px; color: var(--ink);
  }
  .address-band {
    position: absolute; left: 0; top: 1140px; width: 944px; height: 117px;
    background: var(--band-grey);
    display: flex; align-items: center; justify-content: center;
    font-family: "Poppins", sans-serif; font-weight: 500;
    font-size: 30px; color: var(--ink);
  }
</style>
</head>
<body>
  <div class="sign-frame">
    <div class="sign">
      <svg class="sign-shapes" width="944" height="1257" viewBox="0 0 944 1257">
        <defs>
          <linearGradient id="ridgeFill" x1="0" y1="0" x2="0" y2="1">
            <stop offset="0" stop-color="var(--ridge-dark)"/>
            <stop offset="0.5" stop-color="var(--ridge-light)"/>
            <stop offset="1" stop-color="var(--ridge-dark)"/>
          </linearGradient>
          <linearGradient id="tileFill" x1="0" y1="0" x2="1" y2="1">
            <stop offset="0" stop-color="var(--tile-light)"/>
            <stop offset="1" stop-color="var(--tile-dark)"/>
          </linearGradient>
        </defs>
        <polygon class="corner-black" points="0,0 127,0 322,200 0,520" fill="var(--corner-black)"/>
        <polygon class="ridge-cap" points="167,0 527,0 347,177" fill="url(#ridgeFill)"/>
        <polygon class="roof-tiles" role="img" aria-label="Dark roof tile photograph" points="572,0 944,0 944,640 892,690 375,198" fill="url(#tileFill)"/>
      </svg>

      <div class="brand-seal">Delcour<br>Roofing</div>

      <h1 class="company-name"><span>DELCOUR</span><span>ROOFING</span></h1>
      <p class="tagline">Your Hometown Roofing Experts</p>
      <div class="tagline-rule"></div>
      <p class="phone">
        <svg viewBox="0 0 24 24" aria-hidden="true"><path fill="currentColor" d="M6.6 10.8a15.1 15.1 0 0 0 6.6 6.6l2.2-2.2c.3-.3.7-.4 1-.2 1.1.4 2.3.6 3.6.6.6 0 1 .4 1 1V20c0 .6-.4 1-1 1A17 17 0 0 1 3 4c0-.6.4-1 1-1h3.5c.6 0 1 .4 1 1 0 1.3.2 2.5.6 3.6.1.3 0 .7-.2 1z"/><path fill="none" stroke="currentColor" stroke-width="1.8" stroke-linecap="round" d="M14.5 2.5a7 7 0 0 1 7 7M14.5 6a3.5 3.5 0 0 1 3.5 3.5"/></svg>
        <span>337-555-0142</span>
      </p>
      <p class="since">Family Owned Since 1956</p>
      <div class="address-band">438 Fenwick Rd Lake Charles LA 70615</div>
    </div>
  </div>
</body>
</html>
```